Re-Design an adult education portal

I need support to re-design an adult education portal. Currently the customer has an incomplete website which should be prepared in a new format.
I have the idea how to realize, but I have no clue how to design it. The hard thing is to have a "beautiful" website with available logo and main color. I hope you can support me.

Name of Website: tovrenu (tovrenu.ch)
Content: adult eduction for adult in safety at work, mountain climbing, dog school. various courses in different areas. But on old webpage is hard to find the different possibilities.
main color: Ral 6011 (green) -> #6C7C59
logo: you see on top of website the logo (2 dogs and a mountain with a colour gradient).

new website: for new webpage I decided to have a navigation for each section of education. In the main area I would like to have some pictures to give an idea what content is behind. At the moment it looks terrible, so I decided to use you as support for me to make the webpage prettier :). And maybe you have an better idea how to make it great. -> current state of new web page: https://tovrenu.bask-om.ch/

Target Market(s)

adult eduction for adult in safety at work, mountain climbing, dog school

Number of Pages Required

1 page

Font styles to use
Serif
Sans Serif

Requirements
Must have
• As main color is set "Ral 6011" (green) -> #6C7C59

```html
<!DOCTYPE html>
<html lang="de">
<head>
<meta charset="utf-8">
<title>tovrenu – Ausbildungs- und Kurspartner</title>
<link href="https://fonts.googleapis.com/css2?family=Montserrat:wght@400;500;600;700&family=Cormorant+Garamond:wght@400;500&display=swap" rel="stylesheet">
<style>
:root{
  --green:#6c7c59;
  --green-dark:#5d6c4c;
  --white:#ffffff;
  --ink:#1d1d1d;
  --muted:#555;
  --line:#cfcfcf;
  --canvas:#ffffff;
}
*{box-sizing:border-box;margin:0;padding:0}
html,body{width:1200px;height:3750px;overflow:hidden;background:var(--canvas)}
body{font-family:"Montserrat",sans-serif;color:var(--ink);position:relative}
.page{position:absolute;left:138px;top:76px;width:924px;height:3597px;background:var(--white);box-shadow:0 0 24px rgba(0,0,0,.35);overflow:hidden}
.abs{position:absolute}
.btn{position:absolute;background:var(--green);color:var(--white);font-size:10px;font-weight:600;border-radius:14px;display:flex;align-items:center;justify-content:center}
.btn.light{background:var(--white);color:var(--green)}
.photo{position:absolute}

/* top bar */
.topbar{left:0;top:0;width:924px;height:25px;background:var(--green);color:var(--white);font-size:9px;display:flex;align-items:center;justify-content:space-between;padding:0 84px 0 76px}
.topbar .social{display:flex;gap:9px}
.topbar .social span{width:8px;height:8px;border-radius:50%;border:1.3px solid var(--white)}
.nav{left:0;top:25px;width:924px;height:55px;background:var(--white)}
.logo-name{position:absolute;left:68px;top:18px;font-size:17px;font-weight:600;color:var(--green);display:flex;align-items:center;gap:6px}
.logo-name i{width:10px;height:10px;background:var(--green);border-radius:50%;display:block}
.nav-link{position:absolute;top:21px;font-size:10px;color:var(--ink)}
.nav-link.active{text-decoration:underline}

/* hero */
.hero{left:0;top:80px;width:924px;height:468px;background:var(--green);color:var(--white)}
.hero h1{position:absolute;left:68px;top:102px;width:540px;font-size:38px;font-weight:700;line-height:60px;white-space:nowrap}
.hero p{position:absolute;left:68px;top:225px;width:470px;font-size:19px;line-height:31px;font-weight:500}

/* about */
.about-title{left:476px;top:630px;font-size:22px;font-weight:700;border-bottom:1.5px solid var(--ink);padding-bottom:3px}
.about-text{left:476px;top:665px;width:380px;font-size:9.6px;line-height:16.8px;color:var(--muted)}
.divider{left:0;width:924px;height:1px;background:var(--line)}

/* course cards */
.card{position:absolute;left:62px;width:799px;height:230px;background:var(--green);color:var(--white)}
.card .pic{position:absolute;left:33px;top:20px;width:282px;height:188px}
.card h2{position:absolute;left:342px;top:38px;font-size:31px;font-weight:600;white-space:nowrap}
.card h2 small{font-size:21px;font-weight:600}
.card p{position:absolute;left:342px;top:92px;width:400px;font-size:10.5px;line-height:17.4px}

/* features */
.feat-title{font-size:30px;font-weight:600;white-space:nowrap;border-bottom:1.5px solid var(--ink)}
.feat-title small{font-size:21px}
.feat-text{font-size:10px;line-height:16.2px;color:var(--ink)}

/* stats */
.stats{left:0;top:2629px;width:924px;height:185px;background:var(--green);color:var(--white)}
.stat{position:absolute;top:52px;width:240px;text-align:center}
.stat b{display:block;font-family:"Cormorant Garamond",serif;font-weight:400;font-size:36px}
.stat span{font-size:16px}

/* contact */
.contact{left:149px;top:2909px;width:615px;height:378px;border:1.5px solid #d6d6d6;box-shadow:0 3px 8px rgba(0,0,0,.18)}
.contact h2{position:absolute;left:0;width:100%;top:22px;text-align:center;font-size:30px;font-weight:700}
.contact h2 span{border-bottom:2px solid var(--ink)}
.info-card{position:absolute;left:57px;width:157px;height:101px;background:var(--white);box-shadow:0 2px 5px rgba(0,0,0,.25);text-align:center;padding-top:12px}
.info-card .main{font-size:10px;margin-top:4px}
.info-card .small{font-size:5px;line-height:7px;color:var(--muted);padding:2px 18px 0}
.lead{position:absolute;left:282px;font-size:14px}
.field{position:absolute;height:23px;border:1.3px solid #9a9a9a;font-size:10px;color:#aaa;padding:5px 10px}

/* footer */
.footer{left:0;top:3355px;width:924px;height:242px;background:var(--green);color:var(--white)}
.footer .brand{position:absolute;left:68px;top:66px;font-size:28px;font-weight:600;display:flex;align-items:center;gap:10px}
.footer .brand i{width:16px;height:16px;border:2px solid var(--white);border-radius:50%;display:block}
.footer .about{position:absolute;left:68px;top:145px;width:250px;font-size:11px;line-height:17px}
.fcol{position:absolute;top:32px;font-size:11px}
.fcol h4{font-family:"Cormorant Garamond",serif;font-weight:500;font-size:14px;letter-spacing:1px;margin-bottom:14px}
.fcol li{list-style:none;font-size:10px;font-weight:600;margin-bottom:7px}
.fcol li::before{content:"› ";font-weight:400}
.fcol .txt{font-size:9px;line-height:17px}
.news-input{display:flex;margin-top:6px}
.news-input span{width:100px;height:20px;background:var(--white);color:#aaa;font-size:8px;padding:5px 8px}
.news-input b{width:27px;height:20px;border:1px solid var(--white);font-size:8px;display:flex;align-items:center;justify-content:center;margin-left:2px}
</style>
</head>
<body>
<div class="page">

  <div class="abs topbar">
    <span>&#9742; +41 79 000 12 34</span>
    <div class="social"><span></span><span></span><span></span><span></span></div>
  </div>

  <nav class="abs nav">
    <div class="logo-name"><i></i>tovrenu.ch</div>
    <span class="nav-link active" style="left:268px">Home</span>
    <span class="nav-link" style="left:335px">Services</span>
    <span class="nav-link" style="left:411px">Projects</span>
    <span class="nav-link" style="left:487px">Blogs</span>
    <span class="nav-link" style="left:551px">About us</span>
    <span class="nav-link" style="left:631px">Contacts us</span>
    <span class="btn" style="left:749px;top:16px;width:92px;height:24px">More Detail</span>
  </nav>

  <section class="abs hero">
    <h1>Ihr Ausbildungs- und<br>Kurspartner</h1>
    <p>Wir bieten Ihren Wünschen entsprechende Ausbildungen, zielorientiert und Ihrem Können und Wissen angepasst.</p>
    <span class="btn light" style="left:68px;top:323px;width:99px;height:25px">Read More</span>
    <svg class="abs" style="left:570px;top:83px" width="354" height="280">
      <path d="M3 80 V3 H80" fill="none" stroke="#fff" stroke-width="5"/>
      <path d="M3 200 V277 H80" fill="none" stroke="#fff" stroke-width="5"/>
      <rect x="15" y="12" width="339" height="254" fill="#fff"/>
    </svg>
    <div class="photo" role="img" aria-label="Hund läuft durch bunte Slalomstangen auf einer Wiese" style="left:600px;top:110px;width:324px;height:225px;background:linear-gradient(135deg,#c9a53a,#c23a2e 45%,#5d8a3a)"></div>
  </section>

  <div class="photo" style="left:101px;top:645px;width:317px;height:212px;background:#6a6a6a"></div>
  <div class="photo" role="img" aria-label="Sportler beim Hindernistraining auf einem Parcours im Herbst" style="left:87px;top:628px;width:328px;height:213px;background:linear-gradient(160deg,#d9b46a,#8a8a86 50%,#5a5f66)"></div>
  <h2 class="abs about-title">ABOUT US</h2>
  <p class="abs about-text">In meiner Beruflichen Laufbahn erlebte ich immer wieder Situationen, welche in mir die Idee reifen liessen, jedem interessierten Menschen ein Grundwissen zukommen zu lassen, welches ihn bei einer Notsituation richtig und mit der nötigen Ruhe reagieren lässt. Das Zusammenlegen &amp; Kombinieren von Wissen und Fertigkeiten der verschiedenen Fachbereiche gibt dem Menschen Sicherheit und Vertrauen in seinem Handeln. Aus eigener Erfahrung hat sich gezeigt: je professioneller man auf Grenzsituationen vorbereitet ist, desto sicherer und erfolgreicher kann eine Notfallsituation gemeistert und sogar Leben gerettet werden.</p>
  <span class="btn" style="left:476px;top:857px;width:108px;height:24px">Learn More</span>
  <div class="abs divider" style="top:905px"></div>

  <article class="card" style="top:957px">
    <div class="pic" role="img" aria-label="Kletterin mit Helm an einem Felsgrat im Gebirge" style="background:linear-gradient(160deg,#b9c6d3,#7b8470 50%,#4f4a40)"></div>
    <h2>Bergausbildung <small>Bergklettern</small></h2>
    <p>lorem ipsum dolor sit amet, consectetur adipiscing elit. nulla sed cum nunc, egestas placerat vulputate id vitae. a id pellentesque suspendisse tortor mi elementum interdum mauris venenatis.lorem ipsum dolor sit amet, consectetur adipiscing elit. nulla sed cum nunc, egestas placerat vulputate id vitae. a id pellentesque suspendisse tortor mi elementum interdum mauris venenatis.</p>
  </article>

  <article class="card" style="top:1238px">
    <div class="pic" role="img" aria-label="Roter Gabelstapler" style="background:linear-gradient(135deg,#3a3a3a,#c9302c 55%,#2a2a2a)"></div>
    <h2>Staplerkurse <small>Grundausbildung</small></h2>
    <p>lorem ipsum dolor sit amet, consectetur adipiscing elit. nulla sed cum nunc, egestas placerat vulputate id vitae. a id pellentesque suspendisse tortor mi elementum interdum mauris venenatis.lorem ipsum dolor sit amet, consectetur adipiscing elit. nulla sed cum nunc, egestas placerat vulputate id vitae. a id pellentesque suspendisse tortor mi elementum interdum mauris venenatis.</p>
  </article>

  <article class="card" style="top:1520px">
    <div class="pic" role="img" aria-label="Drei Hunde liegen im Gras vor einem Baumstamm im Wald" style="background:linear-gradient(170deg,#4f6a3a,#6b5036 50%,#7fa04a)"></div>
    <h2>Hundeschule <small>Welpenförderung</small></h2>
    <p>lorem ipsum dolor sit amet, consectetur adipiscing elit. nulla sed cum nunc, egestas placerat vulputate id vitae. a id pellentesque suspendisse tortor mi elementum interdum mauris venenatis.lorem ipsum dolor sit amet, consectetur adipiscing elit. nulla sed cum nunc, egestas placerat vulputate id vitae. a id pellentesque suspendisse tortor mi elementum interdum mauris venenatis.</p>
  </article>

  <span class="btn" style="left:753px;top:1772px;width:108px;height:25px">Read More</span>
  <div class="abs divider" style="top:1831px;background:#9a9a9a"></div>

  <div class="photo" role="img" aria-label="Moderner Regionalzug auf einer Bahnstrecke" style="left:62px;top:1888px;width:396px;height:308px;background:linear-gradient(160deg,#a9c4dc,#e6e6e6 45%,#6e8a4a)"></div>
  <h2 class="abs feat-title" style="left:485px;top:1890px">BLS AGD <small>Auffrischungskurs</small></h2>
  <p class="abs feat-text" style="left:488px;top:1940px;width:365px">lorem ipsum dolor sit amet, consectetur adipiscing elit. nulla sed cum nunc, egestas placerat vulputate id vitae. a id pellentesque suspendisse tortor mi elementum interdum mauris venenatis.lorem ipsum dolor sit amet, consectetur adipiscing elit. nulla sed cum nunc, egestas placerat vulputate id vitae. a id pellentesque suspendisse tortor mi elementum interdum mauris venenatislorem ipsum dolor sit amet, consectetur adipiscing elit. nulla sed cum nunc, egestas placerat vulputate id vitae. a id pellentesque suspendisse tortor mi elementum interdum mauris venenatis.lorem ipsum dolor sit amet, consectetur adipiscing elit. nulla sed cum nunc, egestas placerat vulputate id vitae. a id pellentesque suspendisse tortor mi elem</p>
  <span class="btn" style="left:488px;top:2171px;width:109px;height:25px">Read More</span>

  <h2 class="abs feat-title" style="left:62px;top:2250px">CZV <small>Berufsfahrer Weiterbildung</small></h2>
  <p class="abs" style="left:62px;top:2298px;width:380px;font-size:12px;font-weight:700;line-height:18px">Arbeits- und Ruhezeitverordnung ,<br>Eco-Drive ,Fahrzeugtechnik</p>
  <p class="abs feat-text" style="left:65px;top:2343px;width:380px">lorem ipsum dolor sit amet, consectetur adipiscing elit. nulla sed cum nunc, egestas placerat vulputate id vitae. a id pellentesque suspendisse tortor mi elementum interdum mauris venenatis.lorem ipsum dolor sit amet, consectetur adipiscing elit. nulla sed cum nunc, egestas placerat vulputate id vitae. a id pellentesque suspendisse tortor mi elementum interdum mauris venenatislorem ipsum dolor sit amet, consectetur adipiscing elit. nulla sed cum nunc,. a id pellentesque suspendisse tortor mi elementum interdum mauris venenatislorem ipsum dolor sit amet, consectetur adipiscing elit. nulla sed cum nunc,</p>
  <span class="btn" style="left:65px;top:2527px;width:109px;height:24px">Read More</span>
  <div class="photo" role="img" aria-label="Schwarzer Lastwagen mit Anhänger auf einer Landstrasse" style="left:466px;top:2243px;width:396px;height:308px;background:linear-gradient(160deg,#8fb8e0,#1c1f24 45%,#6f9a3f)"></div>

  <section class="abs stats">
    <div class="stat" style="left:116px"><b>112</b><span>ausgebildete Hunde</span></div>
    <div class="stat" style="left:351px"><b>3265</b><span>days of experience</span></div>
    <div class="stat" style="left:584px"><b>23</b><span>Jahre Erfahrung</span></div>
  </section>

  <section class="abs contact">
    <h2><span>CONTACT US</span></h2>
    <div class="info-card" style="top:94px">
      <svg width="34" height="34" viewBox="0 0 24 24"><path d="M6.6 2.5l3 3.5-2 2.2c1.2 2.6 3.4 4.8 6 6l2.2-2 3.6 3-1.6 3.3C11 18.2 5.6 12.8 3.3 4.2z" fill="none" stroke="#1d1d1d" stroke-width="1.2"/></svg>
      <div class="main">+41 79 000 12 34</div>
      <div class="small">Kurze Hinweise zu unseren Zeiten und zur telefonischen Erreichbarkeit hier.</div>
    </div>
    <div class="info-card" style="top:206px">
      <svg width="36" height="28" viewBox="0 0 36 28"><rect x="2" y="3" width="32" height="22" fill="none" stroke="#1d1d1d" stroke-width="1.8"/><path d="M2 3l16 13 16-13" fill="none" stroke="#1d1d1d" stroke-width="1.8"/></svg>
      <div class="main">info@tovrenu.ch</div>
      <div class="small">Schreiben Sie uns jederzeit, wir beantworten jede Anfrage zu unseren Kursen und Ausbildungen rasch.</div>
    </div>
    <p class="lead" style="top:102px">GET STARTED TODAY</p>
    <p class="lead" style="top:128px">SERIOUSLY... IT'S THAT EASY.</p>
    <div class="field" style="left:282px;top:150px;width:264px">email address</div>
    <div class="field" style="left:282px;top:194px;width:128px">first name</div>
    <div class="field" style="left:421px;top:194px;width:125px">last name</div>
    <div class="field" style="left:282px;top:236px;width:128px">company name</div>
    <div class="field" style="left:421px;top:236px;width:125px">phone number</div>
    <span class="btn" style="left:282px;top:279px;width:109px;height:23px">Submit</span>
  </section>

  <footer class="abs footer">
    <div class="brand"><i></i>tovrenu.ch</div>
    <p class="about">Lorem ipsum dolor sit amet, consectetur adipiscing elit. Eu lacus fringilla porttitor pellentesque. Ut nullam sed ultrices</p>
    <div class="fcol" style="left:362px">
      <h4>QUICK LINKS</h4>
      <ul><li>Home</li><li>Services</li><li>Projects</li><li>Blogs</li><li>About Us</li><li>Cntact Us</li></ul>
    </div>
    <div class="fcol" style="left:490px">
      <h4>SOCIAL LINKS</h4>
      <p class="txt">000.000.0000<br><span style="font-size:11px">info@tovrenu.ch</span><br>000.000.000</p>
    </div>
    <div class="fcol" style="left:619px">
      <h4>LOCATION</h4>
      <p class="txt" style="line-height:11px">xxxxxxxxxxxxxxx<br>x<br>xxxxxxx</p>
    </div>
    <div class="fcol" style="left:729px">
      <h4>NEWS LETTER</h4>
      <p style="font-size:6px">Subscribe our news letter</p>
      <div class="news-input"><span>email</span><b>GO</b></div>
    </div>
  </footer>

</div>
</body>
</html>
```